Create an Event-Centric WordPress Website for NGO

1. Project Overview

- We represent "Zusammen für Brockelstedt e.V.", a non-profit association. Our outdated website www.zfbev-verein.de shall get a proper replacement.

- The primary goal of our new site is to showcase and facilitate bookings for our cultural events, including concerts, theme nights, joint dinners and village festivals.

- Alongside event bookings, we plan to introduce the public to our history, values, leadership team, and news through a regularly updated blog.

- At a later stage we aim to integrate a user-friendly web shop based on WooCommerce, offering a range of up to 10 products related to our organization. This web-shop is not part of this project! The only relevant item is to include one menu item called "Shop" in the menu bar within the header.

2. Design Requirements

- The design should lean towards a sleek, welcoming, and slightly playful OnePage layout for the main page with additional pages as required.

- The color scheme should integrate the blue and red from our logo, as detailed in the attached brand board. However, deviations that enhance the design are welcome.

- Essential files like logos, photos, and texts are provided in the attachments.

- Emphasis should be on illustrating the community spirit, our events, and the emotions they evoke.

- Mobile first! Of course we like a great design both on desktops and smartphones. Nevertheless, if priorizaztion is needed, mobiles comes first.

3. Site Structure and Navigation

The website should be structured as follows:

**Main Page:**
- Opening with a Gallery/Video/Slogan.
- Upcoming Events.
- Counters to track event attendance or other metrics.
- Shoet description of what we do incl. mission Statements.
- Team Introduction.
- Top News Highlights.
- Contact Form.

**Additional Pages:**
- **About Us:** Detailing our history, a gallery, and a membership form.
- **Shop:** The content and setup is not part of this project and shall only be displayed as a menu item in the upper menu bar in the header.
- **Data Protection & Imprint:** Accessible via footer links.

Social media buttons for Facebook and Instagram should be prominently placed, preferably in the footer.

I am not really sure, if the design contest includes one page only. For the project please concentrate anyhow on the main page and we can then clarify further details.

4. Technical Requirements

- The site is to be fully developed in WordPress.

- Samples for initial design, including products, news, and events, are attached. However, the end design should accommodate easy edits and content additions. For the news the blog function within WordPress shall be used.

- Usability is paramount. Therefore, the Elementor plugin should be incorporated for easy edits without in-depth technical knowledge.

5. Event Management

- Events should have categories (e.g., concerts, dinner parties).

- Direct ticket booking with a cap on maximum participants is a must. Potential tools include the WordPress plugin TicketNestor or wordpress themes like Galvon. This project only includes the design of the elements related to the event booking on the main page. The setup of the e-commerce functionality Inch. payment, etc. is not part of this project and will be sourced separately at a later stage.

6. Responsiveness & Speed

- The site must be mobile-responsive, ensuring a seamless experience across devices.

- Page load speed is crucial. Optimizations should be made to ensure swift page loads.

7. SEO & Optimization

- The website should be built with basic SEO principles in mind, ensuring improved visibility on search engines.

8. Post-Design

- Upon design completion, a subsequent project will cover the WordPress setup on our VARDEX hosting platform and content addition.

- Continuous direct feedback will be provided throughout the design process to ensure clarity and minimize revisions.

- Post handover, we will manage the site in-house. No long-term maintenance is required from the designer.

9. Additional Notes

- We're open to design deviations if they lead to enhanced outcomes or usability.

10. Sample texts

Main Page:

Opening (Slogan)
[EN]: Slogan for the main opening.
[DE]: "Nachbarschaft spüren. In Brockelstedt daheim!"
Upcoming Events (Event Descriptions)
2.1 Mara Velt
[EN]: Description for Mara Velt's event.
[DE]: "Mara kehrt zurück! Am 10.11.2023 erneut in der Holunderscheune. Lassen Sie sich von ihrem Mix aus Schlagern und Evergreens mitreißen."
2.2 Italienischer Abend
[EN]: Description for the Italian evening.
[DE]: "La Dolce Vita in Brockelstedt. Am 21.11.2023 genießen wir in der Holunderscheune authentische italienische Spezialitäten in einer warmen Atmosphäre."
Metrics (Counters)
[EN]: Counters to showcase community metrics.
[DE]:
Mitglieder: "XXX stolze Mitglieder."
Events in 2023: "XXX Events bisher in diesem Jahr."
Besucher: "XXX glückliche Besucher bei unseren Veranstaltungen."
Short Description (Values and Mission)
[EN]: Short descriptions for the community values.
[DE]:
Miteinander in Brockelstedt stärken: "Unsere Gemeinschaft ist unser Herzstück. Wir setzen uns dafür ein, dass jeder Einwohner in Brockelstedt sich zugehörig und geschätzt fühlt."
Kulturelles Angebot schaffen: "Kultur belebt! Durch Veranstaltungen, Konzerte und Feste bereichern wir das kulturelle Leben in Brockelstedt."
Füreinander da sein: "In guten wie in schlechten Zeiten – wir stehen zusammen. Egal ob jung oder alt, jeder wird in unserer Gemeinschaft unterstützt."
Team (Board Members)
[EN]: Introduction of the board members with photos and titles.
[DE]: "Unser engagiertes Team. Lernen Sie die Köpfe hinter 'Zusammen für Brockelstedt e.V.' kennen."
News (Recent News Highlights)
[EN]: Short description of a recent news event.
[DE]: Sommerfest in Brockelstedt: "Ein voller Erfolg! Mit über 400 Besuchern feierten wir am 21.06.2023 unser traditionelles Sommerfest inklusive Vogelschießen."
Contact Form (Contact Details)
[EN]: Contact form header and description.
[DE]: "Wir sind für Sie da! Haben Sie Fragen, Anregungen oder möchten Sie uns unterstützen? Kontaktieren Sie uns – wir freuen uns auf Ihre Nachricht."

Target Market(s)

Our target audience are the approx. 2.150 citizens of our village based in Germany, east of Hamburg. Many families with children, but also elderly people a singles. Also, foreigners, who are specially interested in our events are considered as our target audience.

Industry/Entity Type

NGO (cultural events for local village community)

Coding

Coded - Design and coding required

Font styles to use
Sans Serif
Other font styles liked:
• We like the combination of OSWALD REGULAR for headlines and MONTSERRAT EXTRA LIGHT or LIGHT for plain text. Deviations which will support a better design are very much welcome.

Colors
0094D4
00A9DD
6FCCEA
C7EBF8
E9F6FB
EB3D1F
EC4F4E
F09395
F8D3D4
FCEDEE

Requirements
Must have
• The design must be adaptable to an event booking function. This can be either achieved by a WordPress plugin such an Event calendar or an Event Wordpress theme (Galvon is preferred). The design shall but mobile first.
Nice to have
• Create an emotional, welcoming atmosphere. More human than streamlining.
Should not have
• We don't like a cold, too straight or too structured design.

```html
<!DOCTYPE html>
<html lang="de">
<head>
<meta charset="utf-8">
<title>Zusammen für Brockelstedt e.V.</title>
<link href="https://fonts.googleapis.com/css2?family=Oswald:wght@400;500;600&family=Montserrat:wght@300;400;500;600&display=swap" rel="stylesheet">
<style>
:root{
  --blue:#0094D4;--blue-dark:#1f4fa3;--blue-2:#00A9DD;--blue-3:#6FCCEA;--blue-4:#C7EBF8;--blue-5:#E9F6FB;
  --red:#EB3D1F;--red-2:#EC4F4E;--red-3:#F09395;--red-4:#F8D3D4;
  --ink:#222;--text:#555;--grey:#f2f2f2;--footer:#2b2b2b;
}
*{box-sizing:border-box;margin:0;padding:0}
html,body{width:1200px;height:4988px;overflow:hidden}
body{font-family:'Montserrat',sans-serif;color:var(--text);background:#fff;position:relative}
h1,h2,h3{font-family:'Oswald',sans-serif;font-weight:500;color:var(--ink)}
.section-title{position:absolute;left:0;width:1200px;text-align:center;font-size:40px;text-transform:uppercase;letter-spacing:.5px}

/* header */
.site-header{position:absolute;top:0;left:0;width:1200px;height:120px;background:#fff;z-index:5}
.logo{position:absolute;left:110px;top:6px;width:210px;height:108px;display:flex;align-items:center;gap:10px}
.logo-mark{width:20px;height:20px;border-radius:50%;background:var(--blue-dark);flex:none}
.logo-name{font-weight:600;font-size:15px;color:var(--blue-dark);line-height:1.2}
.main-nav{position:absolute;left:440px;top:50px;display:flex;gap:28px;font-size:15px;color:#333}
.main-nav .active{color:var(--blue)}
.lang{position:absolute;left:980px;top:50px;font-size:15px;color:var(--blue-dark);font-weight:600}
.btn-red{background:var(--red);color:#fff;font-family:'Oswald',sans-serif;font-size:15px;text-transform:uppercase;border-radius:30px;display:inline-flex;align-items:center;justify-content:center}
.header-cta{position:absolute;left:1046px;top:38px;width:140px;height:46px}

/* hero */
.hero{position:absolute;top:120px;left:0;width:1200px;height:640px;overflow:hidden}
.hero-photo{position:absolute;inset:0;background:linear-gradient(180deg,#c9a58a 0%,#b9835f 25%,#7a5a47 55%,#3e3a35 100%)}
.hero-title{position:absolute;left:70px;top:150px;font-weight:500;font-size:58px;line-height:1.3;color:#fff;text-shadow:0 2px 6px rgba(0,0,0,.35)}
.hero-dots{position:absolute;left:566px;top:570px;display:flex;gap:10px}
.hero-dots span{width:10px;height:10px;border-radius:50%;background:rgba(255,255,255,.6)}
.hero-dots span.on{background:#fff}
.hero-curve{position:absolute;left:0;bottom:0}

/* events */
.event-card{position:absolute;top:940px;width:476px;height:440px;background:#fff;box-shadow:0 4px 16px rgba(0,0,0,.12)}
.event-img{height:216px;background:linear-gradient(135deg,#6a5a4c,#b89a78 60%,#ddc8a8)}
.event-card h3{font-family:'Montserrat',sans-serif;font-weight:600;font-size:22px;padding:40px 24px 14px}
.event-card p{font-size:14px;line-height:1.6;padding:0 24px}

/* metrics */
.metrics{position:absolute;top:1460px;left:0;width:1200px;height:540px;background:linear-gradient(180deg,#dfe4ea,#eceef1)}
.metric{position:absolute;top:180px;width:220px;text-align:center}
.metric-circle{width:160px;height:160px;border-radius:50%;background:#fff;margin:0 auto 18px;box-shadow:0 4px 14px rgba(0,0,0,.1);display:flex;align-items:center;justify-content:center}
.metric h3{font-size:24px;font-weight:400;color:var(--blue-dark)}
.metric p{font-size:14px;line-height:1.5}

/* values */
.values-art{position:absolute;left:80px;top:2100px;width:520px;height:300px}
.values-text{position:absolute;left:672px;top:2160px;width:450px}
.values-text h2{font-size:34px;margin-bottom:18px;text-transform:uppercase}
.values-text p{font-size:13px;line-height:1.75}

/* team */
.team{position:absolute;top:2500px;left:0;width:1200px;height:640px;background:var(--grey)}
.team-sub{position:absolute;top:130px;left:300px;width:600px;text-align:center;font-size:15px;line-height:1.6}
.member{position:absolute;text-align:center}
.member-photo{border-radius:50%;background:linear-gradient(180deg,#a8b4bd,#6c7884);margin:0 auto}
.member-name{font-family:'Oswald',sans-serif;color:#fff;text-transform:uppercase;display:flex;align-items:center;justify-content:center}
.arrow{position:absolute;width:30px;height:30px;border-radius:50%;display:flex;align-items:center;justify-content:center}

/* news */
.news-img{position:absolute;left:192px;top:3260px;width:816px;height:384px;background:linear-gradient(180deg,#3a3f6a,#7a5c8a 45%,#3c3431)}
.news-arrow{position:absolute;top:3420px;width:60px;height:60px;border-radius:50%;background:var(--blue-dark);display:flex;align-items:center;justify-content:center}
.news-date{position:absolute;left:900px;top:3676px;font-size:15px;color:var(--red)}
.news-title{position:absolute;left:192px;top:3760px;font-size:34px}
.news-text{position:absolute;left:192px;top:3836px;font-size:15px;line-height:1.6;width:800px}

/* contact */
.contact{position:absolute;top:3980px;left:0;width:1200px;height:640px;background:linear-gradient(180deg,#e6e8eb,#d6d9de)}
.contact-lead{position:absolute;top:120px;left:300px;width:600px;text-align:center;font-size:15px;line-height:1.6}
.field{position:absolute;background:#fff;border:1px solid #e0e0e0;font-size:13px;color:#888;padding:0 18px;display:flex;align-items:center}
.contact-btn{position:absolute;left:536px;top:520px;width:128px;height:50px}

/* footer */
.site-footer{position:absolute;top:4620px;left:0;width:1200px;height:368px;background:var(--footer);color:#ddd}
.foot-logo{position:absolute;left:108px;top:80px;width:220px;display:flex;align-items:center;gap:10px}
.foot-logo .logo-mark{background:#fff}
.foot-logo span{font-weight:600;font-size:15px;color:#fff;line-height:1.2}
.socials{position:absolute;left:110px;top:200px;display:flex;gap:14px}
.social{width:40px;height:40px;border-radius:50%;border:2px solid var(--red);background:transparent;display:block}
.foot-col{position:absolute;top:70px;font-size:13px;line-height:1.9}
.foot-col h4{font-family:'Oswald',sans-serif;font-weight:400;font-size:16px;color:#fff;text-transform:uppercase;margin-bottom:10px;border-bottom:1px solid #555;padding-bottom:6px}
.copyright{position:absolute;left:420px;top:300px;font-size:13px}
</style>
</head>
<body>

<header class="site-header">
  <div class="logo"><span class="logo-mark"></span><span class="logo-name">Zusammen für Brockelstedt e.V.</span></div>
  <nav class="main-nav"><span class="active">Heim</span><span>Über uns</span><span>Geschäft</span><span>Veranstaltungen</span><span>Kontakt</span></nav>
  <div class="lang">GER ▾</div>
  <a class="btn-red header-cta">Buchen Sie jetzt</a>
</header>

<section class="hero">
  <div class="hero-photo" role="img" aria-label="Reetgedecktes Fachwerkhaus der Holunderscheune im Abendlicht"></div>
  <h1 class="hero-title">Nachbarschaft spüren.<br>In Brockelstedt daheim!</h1>
  <div class="hero-dots"><span class="on"></span><span></span><span></span></div>
  <svg class="hero-curve" width="1200" height="140" viewBox="0 0 1200 140">
    <path d="M0 40 Q600 200 1200 40 L1200 140 L0 140Z" fill="#fff"/>
    <path d="M0 40 Q600 200 1200 40" fill="none" stroke="#1f4fa3" stroke-width="10"/>
  </svg>
</section>

<h2 class="section-title" style="top:828px">Kommende Veranstaltungen</h2>
<article class="event-card" style="left:108px">
  <div class="event-img" role="img" aria-label="Konzertabend mit Publikum in der Holunderscheune"></div>
  <h3>Mara Velt</h3>
  <p>Mara kehrt zurück! Am 10.11.2023 erneut in der Holunderscheune. Lassen Sie sich von ihrem Mix aus Schlagern und Evergreens mitreißen.</p>
</article>
<article class="event-card" style="left:608px">
  <div class="event-img" role="img" aria-label="Gäste an gedeckter Tafel beim italienischen Abend"></div>
  <h3>Italienischer Abend</h3>
  <p>La Dolce Vita in Brockelstedt. Am 21.11.2023 genießen wir in der Holunderscheune authentische italienische Spezialitäten in einer warmen Atmosphäre.</p>
</article>

<section class="metrics" role="img" aria-label="Blass hinterlegtes Foto eines Fachwerkhauses">
  <h2 class="section-title" style="top:76px">Metrics</h2>
  <div class="metric" style="left:210px">
    <div class="metric-circle"><svg width="64" height="64" viewBox="0 0 64 64" fill="none" stroke="#1f4fa3" stroke-width="3"><circle cx="32" cy="22" r="8"/><circle cx="16" cy="28" r="6"/><circle cx="48" cy="28" r="6"/><path d="M18 52c0-9 6-16 14-16s14 7 14 16M4 52c0-7 5-12 12-12M60 52c0-7-5-12-12-12"/></svg></div>
    <h3>Mitglieder</h3><p>Stolze Mitglieder</p>
  </div>
  <div class="metric" style="left:490px">
    <div class="metric-circle"><svg width="64" height="64" viewBox="0 0 64 64" fill="none" stroke="#1f4fa3" stroke-width="3"><rect x="8" y="12" width="48" height="44" rx="4"/><path d="M8 24h48M20 6v12M44 6v12"/><path d="M18 34h6M29 34h6M40 34h6M18 44h6M29 44h6M40 44h6"/></svg></div>
    <h3>Events in 2023</h3><p>Events bisher in diesem Jahr.</p>
  </div>
  <div class="metric" style="left:770px">
    <div class="metric-circle"><svg width="64" height="64" viewBox="0 0 64 64" fill="none" stroke="#1f4fa3" stroke-width="3"><rect x="12" y="14" width="40" height="44" rx="4"/><path d="M26 8h12v10H26z"/><circle cx="32" cy="32" r="6"/><path d="M22 50c0-6 4-9 10-9s10 3 10 9"/></svg></div>
    <h3>Besucher</h3><p>Glückliche Besucher bei unseren Veranstaltungen</p>
  </div>
</section>

<svg class="values-art" viewBox="0 0 520 300" role="img" aria-label="Illustration von Häusern des Dorfes unter einer Kuppel">
  <defs><linearGradient id="dome" x1="0" y1="0" x2="0" y2="1"><stop offset="0" stop-color="#3c4f7a"/><stop offset="1" stop-color="#a9b8d0"/></linearGradient></defs>
  <path d="M60 240 A200 200 0 0 1 460 240 Z" fill="url(#dome)" stroke="#1f4fa3" stroke-width="4"/>
  <path d="M0 240 H520" stroke="#1f4fa3" stroke-width="4"/>
</svg>
<div class="values-text">
  <h2>Werte und Mission</h2>
  <p>Miteinander in Brockelstedt stärken: Unsere Gemeinschaft ist unser Herzstück. Wir setzen uns dafür ein, dass jeder Einwohner in Brockelstedt sich zugehörig und geschätzt fühlt. Kulturelles Angebot schaffen: Kultur belebt! Durch Veranstaltungen, Konzerte und Feste bereichern wir das kulturelle Leben in Brockelstedt. Füreinander da sein: In guten wie in schlechten Zeiten – wir stehen zusammen. Egal ob jung oder alt, jeder wird in unserer Gemeinschaft unterstützt.</p>
</div>

<section class="team">
  <h2 class="section-title" style="top:60px">Team</h2>
  <p class="team-sub">Unser engagiertes Team. Lernen Sie die Köpfe hinter 'Zusammen für Brockelstedt e.V.' kennen.</p>
  <div class="arrow" style="left:64px;top:370px;background:var(--blue-dark)"><svg width="12" height="12" viewBox="0 0 12 12"><path d="M8 1L3 6l5 5" stroke="#fff" stroke-width="2" fill="none"/></svg></div>
  <div class="arrow" style="left:1104px;top:370px;border:2px solid #bbb"><svg width="12" height="12" viewBox="0 0 12 12"><path d="M4 1l5 5-5 5" stroke="#999" stroke-width="2" fill="none"/></svg></div>
  <div class="member" style="left:148px;top:280px;width:200px">
    <div class="member-photo" role="img" aria-label="Porträtfoto Vorstandsmitglied" style="width:200px;height:200px"></div>
    <div class="member-name" style="background:var(--blue-dark);height:44px;font-size:16px;margin-top:-6px">Petra Lindqvist</div>
  </div>
  <div class="member" style="left:448px;top:210px;width:304px">
    <div class="member-photo" role="img" aria-label="Porträtfoto Vorstandsmitglied" style="width:280px;height:280px"></div>
    <div class="member-name" style="background:var(--red);height:60px;font-size:22px;margin-top:-8px">Hanna Roeder</div>
  </div>
  <div class="member" style="left:844px;top:280px;width:200px">
    <div class="member-photo" role="img" aria-label="Porträtfoto Vorstandsmitglied" style="width:200px;height:200px"></div>
    <div class="member-name" style="background:var(--blue-dark);height:44px;font-size:16px;margin-top:-6px">Jonas Ebeling</div>
  </div>
</section>

<h2 class="section-title" style="top:3170px">Nachricht</h2>
<div class="news-img" role="img" aria-label="Gruppenfoto auf der Bühne beim Sommerfest in Brockelstedt"></div>
<div class="news-arrow" style="left:94px"><svg width="18" height="18" viewBox="0 0 18 18"><path d="M12 2L5 9l7 7" stroke="#fff" stroke-width="3" fill="none"/></svg></div>
<div class="news-arrow" style="left:1046px"><svg width="18" height="18" viewBox="0 0 18 18"><path d="M6 2l7 7-7 7" stroke="#fff" stroke-width="3" fill="none"/></svg></div>
<div class="news-date">▦ &nbsp;21.06.2023</div>
<h3 class="news-title">Ein voller Erfolg!</h3>
<p class="news-text">Mit über 400 Besuchern feierten wir am 21.06.2023 unser traditionelles Sommerfest inklusive Vogelschießen.</p>

<section class="contact" role="img" aria-label="Blass hinterlegtes Foto einer Veranstaltung">
  <h2 class="section-title" style="top:52px">Kontaktiere uns</h2>
  <p class="contact-lead">Wir sind für Sie da! Haben Sie Fragen, Anregungen oder möchten Sie uns unterstützen? Kontaktieren Sie uns – wir freuen uns auf Ihre Nachricht.</p>
  <div class="field" style="left:200px;top:216px;width:390px;height:56px">Vorname</div>
  <div class="field" style="left:610px;top:216px;width:390px;height:56px">Nachname</div>
  <div class="field" style="left:200px;top:296px;width:390px;height:56px">eMail</div>
  <div class="field" style="left:610px;top:296px;width:390px;height:56px">Telefonnummer</div>
  <div class="field" style="left:200px;top:376px;width:800px;height:100px;align-items:flex-start;padding-top:18px">Nachricht</div>
  <a class="btn-red contact-btn">Einreichen</a>
</section>

<footer class="site-footer">
  <div class="foot-logo"><span class="logo-mark"></span><span>Zusammen für Brockelstedt e.V.</span></div>
  <div class="socials"><span class="social" aria-label="Soziales Netzwerk"></span><span class="social" aria-label="Soziales Netzwerk"></span></div>
  <div class="foot-col" style="left:420px;width:200px"><h4>Visit us</h4>Dorfstraße 12<br>21514 Brockelstedt</div>
  <div class="foot-col" style="left:680px;width:190px"><h4>Contact us</h4>+49 4151 220 480<br>info@zfbev-verein.de</div>
  <div class="foot-col" style="left:900px;width:200px;line-height:1.55"><h4>Quick links</h4>Heim<br>Über uns<br>Geschäft<br>Veranstaltungen<br>Kontakt<br>Links zum Datenschutz<br>Impressum</div>
  <div class="copyright">2023 zfbev. All Rights Reserved.</div>
</footer>

</body>
</html>
```